Cocktail Reception Invitation - For New Office Location

We are a residential property management, investment, and acquisition company and we have recently moved to a new corporate headquarters. We are hosting an event for current customers/vendors, as well as prospects, to show off the new office and enhance the legitimacy of our brand. The event will be a cocktail reception with heavy appetizers/hors d'oeuvres and a bar. We want the invitation to be professional, clean, and somewhat modern. Would be great if we could have it formatted for both electronic delivery AND print, but print is the priority. Thanks in advance for submitting! Photo of the new building attached - does not have to be on the invitation though.

Target Market(s)

Investors, Property Owners, Contractors

Industry/Entity Type

Real Estate

Requirements
Must have
• Must have placeholders for event date, time, location, RSVP, etc. Date is Thursday November 17th from 4-7:00 PM at 418 W Harlow St, Indianapolis, IN 46219. The invitees are a very professional group of people and the invitation should be classy and clean.
Nice to have
• Our colors are Navy Blue, Orange, and dark gray. Not required if it doesn't look good on the invite but it might be nice. I have included a photo of the new office if it makes sens to have it on the invitation.

```html
<!DOCTYPE html>
<html lang="en">
<head>
<meta charset="utf-8">
<title>Cocktail Party Invitation</title>
<link rel="stylesheet" href="https://fonts.googleapis.com/css2?family=PT+Sans:wght@400&family=Pinyon+Script&display=swap">
<style>
  :root {
    --navy: #0808a3;
    --panel-gray: #b3b3b3;
    --dot-gray: #8c8c8c;
    --text-light: #c6c6d2;
    --orange: #f7941d;
    --ink: #141414;
    --rule-white: #f2f0ea;
  }
  html, body {
    margin: 0;
    padding: 0;
    width: 1200px;
    height: 1200px;
    overflow: hidden;
    background: var(--navy);
  }
  .invitation {
    position: relative;
    width: 1200px;
    height: 1200px;
    font-family: "PT Sans", Arial, sans-serif;
  }
  .invitation__frame {
    position: absolute;
    inset: 0;
  }
  .line {
    position: absolute;
    left: 0;
    width: 1200px;
    margin: 0;
    text-align: center;
    line-height: 1;
    white-space: nowrap;
    font-weight: 400;
  }
  .lead-in {
    top: 277px;
    font-size: 27px;
    letter-spacing: 0.6px;
    color: var(--text-light);
    text-transform: uppercase;
  }
  .event-title {
    top: 350px;
    font-family: "Pinyon Script", cursive;
    font-size: 84px;
    color: var(--orange);
    letter-spacing: -1px;
  }
  .venue-intro {
    top: 477px;
    font-size: 27px;
    letter-spacing: 0.6px;
    color: var(--text-light);
    text-transform: uppercase;
  }
  .address {
    top: 547px;
    font-size: 39px;
    line-height: 43px;
    color: var(--text-light);
    font-variant: small-caps;
  }
  .schedule {
    top: 667px;
    font-size: 32px;
    line-height: 38px;
    color: var(--orange);
    font-variant: small-caps;
  }
  .rsvp-heading {
    top: 910px;
    font-family: "Pinyon Script", cursive;
    font-size: 78px;
    color: var(--navy);
  }
  .rsvp-contact {
    top: 1013px;
    font-size: 35px;
    color: var(--ink);
    font-variant: small-caps;
  }
</style>
</head>
<body>
<main class="invitation">
  <svg class="invitation__frame" width="1200" height="1200" viewBox="0 0 1200 1200" aria-hidden="true">
    <rect x="0" y="0" width="1200" height="1200" fill="var(--navy)"/>
    <rect x="32" y="32" width="1136" height="1136" fill="var(--panel-gray)"/>
    <rect x="72" y="72" width="1056" height="1056" fill="none" stroke="#333" stroke-width="2" stroke-dasharray="2 2"/>
    <rect x="79" y="79" width="1042" height="1042" fill="none" stroke="var(--navy)" stroke-width="6"/>
    <rect x="88" y="88" width="1024" height="1024" fill="none" stroke="var(--rule-white)" stroke-width="2"/>
    <circle cx="600" cy="504" r="358" fill="var(--navy)"/>
    <circle cx="600" cy="504" r="332" fill="none" stroke="var(--dot-gray)" stroke-width="8" stroke-linecap="round" stroke-dasharray="0 23.18"/>
  </svg>

  <p class="line lead-in">You are invited to a</p>
  <h1 class="line event-title">Cocktail Party</h1>
  <p class="line venue-intro">at our new office at</p>
  <p class="line address">418 W Harlow St,<br>Indianapolis, IN 46219</p>
  <p class="line schedule">Thursday | November 17, 2016<br>4:00 PM to 7:00 PM</p>
  <h2 class="line rsvp-heading">Rsvp</h2>
  <p class="line rsvp-contact">to Lena Ross | 0321.654.9870</p>
</main>
</body>
</html>
```